New Website for novelty yarn producer

We need a new website for our company, Tarvek. We make highly tailored yarns for weavers worldwide. This year marks our 40th anniversary and we want to evolve our image and identity.

Our temporary website can be found at:
www.tarvekyarns.com

Our only concern in that throughout the website the protagonist must be our client, we make their creations possible and are highly adaptable both during the ideation process of the yarn as well as in the production. This is at the core of the way we do business and is summarised within the concept of FPM (Fluid Partner Method).

Industry/Entity Type

Textile

Number of Pages Required

1 page

Colors
9bcb3c

Requirements
Must have
• Fluid Partner Method (FPM) - can be found on or current website www.tarvekyarns.com

```html
<!DOCTYPE html>
<html lang="en">
<head>
<meta charset="utf-8">
<title>Tarvek Novelty Yarn Solution</title>
<link rel="stylesheet" href="https://fonts.googleapis.com/css2?family=Playfair+Display:wght@700;900&family=Poppins:wght@400;500;600;700&display=swap">
<style>
:root{
  --green:#9bcb3c;
  --green-dark:#7fae28;
  --ink:#222;
  --text:#555;
  --red:#b3151c;
  --red-dark:#6e0a0e;
  --dark:#1c1c1c;
  --dark-2:#2a2a2a;
  --blue:#4cc3ea;
  --orange:#ee4a22;
  --white:#fff;
}
*{box-sizing:border-box;margin:0;padding:0}
html,body{width:1200px;height:3844px;overflow:hidden}
body{font-family:'Poppins',sans-serif;color:var(--text);background:var(--white);position:relative;font-size:14px;line-height:1.6}
.serif{font-family:'Playfair Display',serif}
section,header,footer,nav{position:absolute;left:0;width:1200px}

/* header */
.topbar{top:0;height:120px;background:var(--white)}
.brand{position:absolute;left:172px;top:22px;font-family:'Poppins',sans-serif;font-weight:700;font-size:46px;letter-spacing:2px;color:var(--ink);line-height:1}
.brand-sub{position:absolute;left:174px;top:76px;font-size:11px;letter-spacing:3px;color:var(--ink)}
.call{position:absolute;right:120px;top:38px;display:flex;align-items:center;gap:14px}
.call-icon{width:40px;height:40px;border-radius:8px;background:var(--ink);display:flex;align-items:center;justify-content:center}
.call small{display:block;font-size:13px;color:var(--text);line-height:1.2}
.call strong{font-size:22px;color:var(--ink);line-height:1.2}
.mainnav{top:120px;height:40px;background:var(--green);display:flex;justify-content:center;gap:44px;align-items:center}
.mainnav a{color:var(--ink);font-weight:600;font-size:13px;text-decoration:none;letter-spacing:.5px}

/* hero */
.hero{top:160px;height:460px;background:linear-gradient(160deg,#5c1014 0%,#a51b22 30%,#8d8b86 55%,#4a2326 80%,#2a1214 100%)}
.hero-title{position:absolute;top:20px;width:100%;text-align:center;color:var(--white);font-size:48px;line-height:1.12;text-shadow:0 2px 6px rgba(0,0,0,.4)}
.hero-badge{position:absolute;left:526px;top:150px;width:148px;height:148px;border-radius:50%;border:4px solid var(--white)}

/* welcome */
.welcome{top:620px;height:372px}
.welcome h1{position:absolute;left:172px;top:44px;font-size:30px;line-height:1.15;color:var(--ink)}
.welcome .copy{position:absolute;left:172px;top:130px;width:600px;font-size:12.5px}
.welcome .copy p{margin-bottom:16px}
.welcome-badge{position:absolute;left:870px;top:70px;width:160px;height:160px;border-radius:50%;border:5px solid var(--ink)}

/* values */
.values{top:992px;height:440px;background:linear-gradient(180deg,var(--red-dark),var(--red) 40%,#8c1016)}
.card{position:absolute;top:64px;width:262px;height:300px;background:var(--white);border-radius:4px;overflow:hidden;box-shadow:0 4px 12px rgba(0,0,0,.3)}
.card h3{background:var(--green);color:var(--white);font-family:'Playfair Display',serif;font-size:18px;font-weight:700;padding:10px 18px;letter-spacing:.5px;white-space:nowrap}
.card p{padding:26px 22px;text-align:center;font-size:12.5px}

/* production */
.production{top:1432px;height:500px}
.panel{position:absolute;top:40px;width:418px;height:420px;border-radius:6px;overflow:hidden}
.panel-green{left:172px;background:var(--green);color:var(--white)}
.panel-green h2{text-align:center;font-size:25px;line-height:1.15;margin-top:26px}
.method{display:flex;align-items:center;gap:18px;margin:34px 0 0 60px}
.method-mark{width:92px;height:92px;border-radius:50%;border:6px solid var(--white)}
.method-name{font-size:22px;line-height:1.2;letter-spacing:1px}
.panel-green p{text-align:center;font-size:12.5px;padding:30px 40px 0}
.btn{display:inline-block;background:var(--white);color:var(--ink);font-size:11px;font-weight:600;padding:8px 18px;border-radius:3px;letter-spacing:.5px}
.panel .btn-wrap{text-align:center;margin-top:16px}
.panel-photo{left:612px;background:linear-gradient(135deg,#0f1418,#1d3a4a 40%,#8a3a1f 70%,#111 100%)}
.panel-photo .over{position:absolute;inset:0;padding:44px 40px;color:var(--white);text-align:center;font-size:13px;background:rgba(0,0,0,.35)}
.panel-photo .over p{margin-bottom:14px}

/* offer */
.offer{top:1932px;height:468px;background:linear-gradient(180deg,var(--dark-2),var(--dark))}
.offer h2{position:absolute;top:22px;width:100%;text-align:center;color:var(--green);font-size:44px}
.service{position:absolute;top:130px;width:260px;text-align:center;color:var(--white)}
.service .ico{width:120px;height:120px;border-radius:50%;background:var(--green);margin:0 auto 18px;display:flex;align-items:center;justify-content:center}
.service h3{font-size:19px;font-weight:600;margin-bottom:6px}
.service p{font-size:12.5px;color:#ddd}

/* numbers */
.numbers{top:2400px;height:220px;background:var(--blue)}
.numbers h2{position:absolute;left:172px;top:44px;color:var(--ink);font-size:24px;font-weight:500;line-height:1.2}
.numbers .btn{position:absolute;left:172px;top:130px}
.stat{position:absolute;top:36px;width:180px;height:150px;background:var(--white);text-align:center;padding-top:22px;color:var(--ink)}
.stat strong{display:block;font-size:54px;font-weight:600;line-height:1}
.stat span{display:block;font-size:11px;font-weight:600;margin-top:12px;line-height:1.3}

/* testimonials */
.reviews{top:2620px;height:380px}
.reviews h2{position:absolute;top:44px;width:100%;text-align:center;color:var(--ink);font-size:26px}
.review{position:absolute;top:140px;width:470px;display:flex;gap:24px}
.portrait{width:120px;height:120px;flex:none;transform:rotate(45deg);margin:20px;background:linear-gradient(135deg,#c9b49a,#7a8a70);border:4px solid var(--green)}
.review blockquote{font-size:12.5px;font-style:italic;padding-top:6px}
.review cite{display:block;margin-top:8px;font-style:normal;color:var(--green-dark);font-weight:600;font-size:13px}

/* video */
.cta{top:3200px;height:312px;background:var(--green)}
.video{top:3008px;left:360px;width:480px;height:280px;background:linear-gradient(135deg,#0f3a4a,#2b7ba0 45%,#13262f);box-shadow:0 6px 16px rgba(0,0,0,.3)}
.video svg{position:absolute;left:210px;top:110px}
.cta-text{position:absolute;top:112px;width:100%;text-align:center;color:var(--white);font-size:22px;line-height:1.4}
.cta-btn{position:absolute;top:216px;left:444px;width:312px;height:44px;border-radius:24px;background:var(--orange);color:var(--white);font-weight:600;font-size:16px;display:flex;align-items:center;justify-content:center;gap:10px}

/* footer */
.site-footer{top:3512px;height:332px;background:linear-gradient(180deg,#222,#111);color:#bbb;font-size:11px}
.f-brand{position:absolute;left:172px;top:40px;color:var(--white);font-weight:700;font-size:40px;letter-spacing:2px;line-height:1}
.f-address{position:absolute;left:172px;top:110px;width:190px;line-height:1.7}
.f-col{position:absolute;top:40px}
.f-col h4{color:var(--green);font-size:12px;font-weight:600;margin-bottom:10px}
.f-col li{list-style:none;line-height:1.9}
.signup{display:flex;margin-top:14px}
.signup span{width:150px;height:28px;background:var(--white);color:#999;padding:5px 8px}
.signup-btn{display:inline-block;margin-top:8px;background:var(--green);color:var(--white);padding:5px 14px;font-weight:600}
.socials{display:flex;gap:8px;margin-top:12px}
.socials i{width:26px;height:26px;border-radius:50%;border:2px solid #bbb;display:block}
.copyright{position:absolute;left:0;bottom:0;width:100%;height:48px;border-top:1px solid #333;text-align:center;line-height:48px;font-size:11px}
</style>
</head>
<body>

<header class="topbar">
  <div class="brand">TARVEK</div>
  <div class="brand-sub">NOVELTY YARN SOLUTION</div>
  <div class="call">
    <div class="call-icon">
      <svg width="20" height="20" viewBox="0 0 24 24"><path fill="#9bcb3c" d="M6.6 10.8a15 15 0 0 0 6.6 6.6l2.2-2.2a1 1 0 0 1 1-.25 11.4 11.4 0 0 0 3.6.57 1 1 0 0 1 1 1V20a1 1 0 0 1-1 1A17 17 0 0 1 3 4a1 1 0 0 1 1-1h3.5a1 1 0 0 1 1 1c0 1.25.2 2.45.57 3.570a1 1 0 0 1-.25 1z"/></svg>
    </div>
    <div><small>Call Us</small><strong>0590 41827</strong></div>
  </div>
</header>

<nav class="mainnav">
  <a>HOME</a><a>ABOUT US</a><a>FLUID PARTNER METHOD</a><a>HERITAGE</a><a>TEAM</a><a>BLOG</a><a>CONTACT</a>
</nav>

<section class="hero" role="img" aria-label="Close-up photograph of colourful woven yarn samples with an anniversary badge">
  <h2 class="hero-title serif">Tailored Weaving<br>Solutions</h2>
  <div class="hero-badge"></div>
</section>

<section class="welcome">
  <h1 class="serif">WELCOME TO<br>TARVEK NOVELTY YARN SOLUTION</h1>
  <div class="copy">
    <p>2017 is the 40th anniversary which calls for celebration and a new project. Tarvek Novelty Yarn Solution brings together 40 years of heritage and tradition in listening to and developing, innovating and taking on challenges.</p>
    <p>All the experience and the heritage of the two companies are acquired by a single young team that combines skills to create a new foundation for the future: the Fluid Partner Method, an approach that unites knowledge and experience, and puts our clients at the centre of everything we do.</p>
  </div>
  <div class="welcome-badge"></div>
</section>

<section class="values" role="img" aria-label="Close-up photograph of red yarn threads as background">
  <div class="card" style="left:172px"><h3>EXPERIENCE</h3><p>Over the years the company has gained the knowledge and skills that define the expertise of our production and the quality of our work today.</p></div>
  <div class="card" style="left:470px"><h3>CREATIVITY</h3><p>Our talent is that the way to our clients' success is a combination of innovation, creativity and quality. We strive to adapt, look for new ideas and develop each yarn with care for every client's demands.</p></div>
  <div class="card" style="left:768px"><h3>PROFESSIONALISM</h3><p>We are a family business at the core. Our company is run with the same values as the early family: respect, determination and commitment.</p></div>
</section>

<section class="production">
  <div class="panel panel-green">
    <h2 class="serif">PRODUCTION BUILT<br>AROUND YOU</h2>
    <div class="method"><div class="method-mark"></div><div class="method-name">FLUID PARTNER<br>METHOD</div></div>
    <p>Versatility and flexibility meet a management and production journey delivering our clients' creations to life in one seamless way.</p>
    <div class="btn-wrap"><span class="btn">FIND OUT MORE ›</span></div>
  </div>
  <div class="panel panel-photo" role="img" aria-label="Photograph of coloured yarn cones in a dark warehouse">
    <div class="over">
      <p>Our team has decades of experience in providing yarn solutions to weavers around the world, assisting them in the creation of outstanding fabrics.</p>
      <p>Our clients can expect open lines of communication, clarity and professionalism.</p>
      <p>Our focus is our client.<br>The success of a client is our success.</p>
      <div class="btn-wrap"><span class="btn">OUR HERITAGE ›</span></div>
    </div>
  </div>
</section>

<section class="offer">
  <h2 class="serif">WHAT WE OFFER</h2>
  <div class="service" style="left:180px">
    <div class="ico"><svg width="60" height="60" viewBox="0 0 60 60" fill="none" stroke="#fff" stroke-width="3"><circle cx="30" cy="30" r="7"/><circle cx="30" cy="8" r="5"/><circle cx="30" cy="52" r="5"/><circle cx="9" cy="19" r="5"/><circle cx="51" cy="19" r="5"/><circle cx="9" cy="41" r="5"/><circle cx="51" cy="41" r="5"/><path d="M30 13v10M30 37v10M13 21l11 6M47 21l-11 6M13 39l11-6M47 39l-11-6"/></svg></div>
    <h3>Network</h3><p>A network of weavers, yarn producers and representatives consolidated over 40 years of successful business operations.</p>
  </div>
  <div class="service" style="left:470px">
    <div class="ico"><svg width="60" height="60" viewBox="0 0 60 60" fill="none" stroke="#fff" stroke-width="3"><circle cx="30" cy="30" r="22"/><path d="M8 30h44M30 8c-8 8-8 36 0 44M30 8c8 8 8 36 0 44"/></svg></div>
    <h3>Logistics</h3><p>With a distribution grid organised and tuned to perfection we bring your yarns where you need them, when you need them.</p>
  </div>
  <div class="service" style="left:760px">
    <div class="ico"><svg width="60" height="60" viewBox="0 0 60 60" fill="none" stroke="#fff" stroke-width="3"><path d="M8 50V28l12 8v-8l12 8v-8l12 8V12h8v38z"/><path d="M16 44h6M28 44h6M40 44h6"/></svg></div>
    <h3>Production</h3><p>Production has a dynamic and solid, striving for freedom as well as precision in any project.</p>
  </div>
</section>

<section class="numbers">
  <h2>TYS in Numbers<br>2017</h2>
  <span class="btn">FIND OUT MORE ›</span>
  <div class="stat" style="left:400px"><strong>40</strong><span>YEARS IN BUSINESS</span></div>
  <div class="stat" style="left:640px"><strong>2</strong><span>MILLION<br>KILOGRAMS / YR</span></div>
  <div class="stat" style="left:860px"><strong>40</strong><span>BRANDS</span></div>
</section>

<section class="reviews">
  <h2 class="serif">WHAT PEOPLE ARE SAYING ABOUT US</h2>
  <div class="review" style="left:150px">
    <div class="portrait" role="img" aria-label="Portrait photograph of a client"></div>
    <blockquote>"Lorem ipsum dolor sit amet, consectetur adipiscing elit, sed do eiusmod tempor incididunt ut labore et dolore magna aliqua. Ut enim ad minim veniam quis nostrud exercitation ullamco laboris nisi ut aliquip ex ea commodo consequat."<cite>Marco Velin</cite></blockquote>
  </div>
  <div class="review" style="left:630px">
    <div class="portrait" role="img" aria-label="Portrait photograph of a client"></div>
    <blockquote>"Lorem ipsum dolor sit amet, consectetur adipiscing elit, sed do eiusmod tempor incididunt ut labore et dolore magna aliqua. Ut enim ad minim veniam quis nostrud exercitation ullamco laboris nisi ut aliquip ex ea commodo consequat."<cite>Luca Dorne</cite></blockquote>
  </div>
</section>

<section class="cta">
  <p class="cta-text">Lorem ipsum dolor sit amet, consectetur adipiscing elit, sed do<br>eiusmod tempor incididunt ut labore et dolore magna aliqua.</p>
  <div class="cta-btn"><svg width="18" height="18" viewBox="0 0 18 18"><circle cx="9" cy="9" r="8" fill="none" stroke="#fff" stroke-width="2"/><path d="M7 5l4 4-4 4" fill="none" stroke="#fff" stroke-width="2"/></svg>DISCOVER HOW WE CAN HELP</div>
</section>

<section class="video" role="img" aria-label="Video still of blue patterned woven fabric">
  <svg width="60" height="60" viewBox="0 0 60 60"><circle cx="30" cy="30" r="28" fill="rgba(255,255,255,.85)"/><path d="M24 18l18 12-18 12z" fill="#1c1c1c"/></svg>
</section>

<footer class="site-footer">
  <div class="f-brand">TARVEK</div>
  <p class="f-address">Tarvek S.r.l.<br>Via delle Filande 14, 22100 Como<br>Tel +39 0590 41827<br>Fax +39 0590 41828<br>VAT 01234560987<br>Share capital € 120.000</p>
  <div class="f-col" style="left:500px"><h4>Quick Links</h4><ul><li>Home</li><li>About Us</li><li>Fluid Partner Method</li><li>Heritage</li><li>Team</li><li>Blog</li><li>Contact</li></ul></div>
  <div class="f-col" style="left:690px;width:200px"><h4>Sign Up For Newsletter</h4><p>Stay connected and receive news updates from Tarvek Novelty Yarn Solution.</p><div class="signup"><span>Enter email here</span></div><span class="signup-btn">SIGN UP</span></div>
  <div class="f-col" style="left:900px"><h4>Contact Us</h4><ul><li>Phone</li><li style="color:#fff">0590 41827</li><li>Fax</li><li style="color:#fff">0590 41862</li></ul><div class="socials"><i></i><i></i><i></i></div></div>
  <div class="copyright">© 2018 Novelty Yarn Solutions. All rights reserved.</div>
</footer>

</body>
</html>
```